The Perfect Business Card for PineHarbor

I am looking for a business card which beautifully incorporates my logo, reflects my business and looks special, elegant and clean.

```html
<!DOCTYPE html>
<html lang="en">
<head>
<meta charset="utf-8">
<title>PineHarbor Business Card</title>
<link href="https://fonts.googleapis.com/css2?family=Montserrat:wght@400;500;600;700&display=swap" rel="stylesheet">
<style>
  :root {
    --page: #ffffff;
    --green-light: #8fbb68;
    --green: #76a243;
    --green-deep: #4f6f2c;
    --ink: #2a2c38;
    --ink-soft: #4a4c55;
    --paper: #fbfbfa;
    --font: "Montserrat", Arial, sans-serif;
  }
  * { margin: 0; padding: 0; box-sizing: border-box; }
  html, body { width: 687px; height: 1200px; overflow: hidden; background: var(--page); font-family: var(--font); }
  .canvas { position: relative; width: 687px; height: 1200px; }
  .card {
    position: absolute; left: 43px; width: 600px; height: 343px; overflow: hidden;
    box-shadow: 0 3px 10px rgba(0,0,0,0.22);
  }
  .card-front { top: 210px; }
  .card-back { top: 632px; background: var(--paper); }
  .card-art { position: absolute; inset: 0; width: 100%; height: 100%; }

  .brand {
    position: absolute; left: 0; right: 0; top: 142px;
    display: flex; align-items: center; justify-content: center; gap: 14px;
  }
  .brand-dot { width: 16px; height: 16px; border-radius: 50%; background: #ffffff; }
  .brand-name { color: #ffffff; font-size: 44px; font-weight: 500; letter-spacing: 0.5px; }
  .front-url {
    position: absolute; left: 342px; top: 292px; color: #ffffff; font-size: 15.5px; letter-spacing: 0.4px;
  }
  .front-url-rule {
    position: absolute; left: 340px; top: 318px; width: 180px; height: 1px;
    background: linear-gradient(90deg, rgba(255,255,255,0), rgba(255,255,255,0.8), rgba(255,255,255,0));
  }

  .person { position: absolute; left: 53px; top: 57px; }
  .person-name { font-size: 21px; font-weight: 700; letter-spacing: 0.6px; color: var(--ink); }
  .person-name .first { color: var(--green); }
  .person-role { margin-top: 5px; margin-left: 3px; font-size: 10.5px; font-weight: 600; letter-spacing: 1.1px; color: var(--ink); }

  .credentials { position: absolute; left: 50px; top: 140px; width: 290px; }
  .credentials-title { font-size: 11px; font-weight: 700; letter-spacing: 0.6px; color: var(--ink); }
  .credentials-text { margin-top: 3px; font-size: 8.3px; line-height: 1.32; color: var(--ink-soft); }

  .contacts { position: absolute; left: 49px; top: 208px; list-style: none; }
  .contacts li { display: flex; align-items: center; gap: 9px; height: 21px; font-size: 11.5px; font-weight: 500; color: var(--ink-soft); }
  .contacts svg { width: 13px; height: 13px; flex: none; }

  .back-brand {
    position: absolute; left: 345px; top: 48px; width: 240px; height: 240px; border-radius: 50%;
    background: #ffffff; border: 2px solid var(--green);
    box-shadow: 0 6px 12px rgba(0,0,0,0.12);
    display: flex; align-items: center; justify-content: center;
  }
  .back-brand-name { color: var(--green); font-size: 26px; font-weight: 500; }
</style>
</head>
<body>
<div class="canvas">

  <section class="card card-front" aria-label="Business card front">
    <svg class="card-art" viewBox="0 0 600 343" preserveAspectRatio="none" aria-hidden="true">
      <defs>
        <linearGradient id="frontFill" x1="0" y1="0" x2="0" y2="1">
          <stop offset="0" stop-color="#8fbb68"/>
          <stop offset="1" stop-color="#6f9c3e"/>
        </linearGradient>
      </defs>
      <rect width="600" height="343" fill="url(#frontFill)"/>
      <path d="M0 258 C120 290 260 255 390 250 C470 247 540 260 600 300 L600 343 L0 343 Z" fill="#79a548"/>
      <path d="M0 252 C120 285 260 250 390 244 C470 241 540 255 600 284 L600 300 C540 262 470 250 390 254 C260 260 120 292 0 276 Z" fill="var(--green-deep)"/>
      <path d="M0 262 C50 240 75 200 65 165" stroke="rgba(255,255,255,0.1)" stroke-width="2" fill="none"/>
      <path d="M60 0 C50 30 30 52 0 68" stroke="var(--green-deep)" stroke-opacity="0.45" stroke-width="3" fill="none"/>
    </svg>
    <div class="brand">
      <span class="brand-dot"></span>
      <span class="brand-name">PineHarbor</span>
    </div>
    <p class="front-url">www.pineharbor.ch/en/</p>
    <div class="front-url-rule"></div>
  </section>

  <section class="card card-back" aria-label="Business card back">
    <svg class="card-art" viewBox="0 0 600 343" preserveAspectRatio="none" aria-hidden="true">
      <path d="M0 304 C150 300 300 270 420 232 C500 207 560 230 600 248 L600 343 L0 343 Z" fill="var(--green)"/>
      <path d="M0 300 C150 296 300 266 420 228 C500 203 560 226 600 244 L600 256 C560 238 500 216 420 240 C300 278 150 308 0 318 Z" fill="var(--green-deep)"/>
      <path d="M66 0 C52 30 30 56 0 72" stroke="var(--green)" stroke-opacity="0.5" stroke-width="3" fill="none"/>
    </svg>

    <div class="person">
      <h1 class="person-name"><span class="first">DR. MAREN</span> HOLLOWAY</h1>
      <p class="person-role">WORK &amp; ORGANIZATIONAL PSYCHOLOGIST</p>
    </div>

    <div class="credentials">
      <h2 class="credentials-title">CERTIFIED NATUROPATH</h2>
      <p class="credentials-text">(THN – Traditional Herbal Naturopathy), Certified Coach,<br>Ayurvedic Practitioner, Certified Clinical Hypnotherapist,<br>Restorative Yoga Therapist.</p>
    </div>

    <ul class="contacts">
      <li>
        <svg viewBox="0 0 24 24" aria-hidden="true"><path d="M6.6 10.8a15 15 0 0 0 6.6 6.6l2.2-2.2a1 1 0 0 1 1-.25 11.4 11.4 0 0 0 3.6.6 1 1 0 0 1 1 1V20a1 1 0 0 1-1 1A17 17 0 0 1 3 4a1 1 0 0 1 1-1h3.5a1 1 0 0 1 1 1c0 1.25.2 2.45.6 3.6a1 1 0 0 1-.25 1z" fill="#6e9a3b"/></svg>
        +41 (0)76 555 01 23
      </li>
      <li>
        <svg viewBox="0 0 24 24" aria-hidden="true"><rect x="2" y="5" width="20" height="14" fill="#6e9a3b"/><path d="M2 5l10 8 10-8" stroke="#ffffff" stroke-width="1.6" fill="none"/></svg>
        info@pineharbor.ch
      </li>
      <li>
        <svg viewBox="0 0 24 24" aria-hidden="true"><circle cx="12" cy="12" r="9.5" fill="none" stroke="#6e9a3b" stroke-width="2"/><path d="M2.5 12h19M12 2.5c3 3 3 16 0 19M12 2.5c-3 3-3 16 0 19" stroke="#6e9a3b" stroke-width="1.5" fill="none"/></svg>
        www.pineharbor.ch/en/
      </li>
    </ul>

    <div class="back-brand">
      <span class="back-brand-name">PineHarbor</span>
    </div>
  </section>

</div>
</body>
</html>
```